Moden - Bajaflor - Flower Shop

brisapetals is looking for a cool web design that has a airy, clean, mexicali feel to it.

See attached images and links for idea of what we mean with the above.

please no templates.
Updates

Target Market(s)

Local flower shop in San Diego, California

Industry/Entity Type

Shop

Requirements
Must have
• see. brisapetals.quillcart.example - I did the site and logo...I love the logo - hate the site.

Going for this feel: http://www.plumnotebook.example/tablecraft/archives/verandos.php

I also attached another site I liked- I just feel like it may be to busy.

```html
<!DOCTYPE html>
<html lang="en">
<head>
<meta charset="utf-8">
<title>Brisa Petals — Bajaflor Spring Collection</title>
<link href="https://fonts.googleapis.com/css2?family=Arvo:wght@400;700&family=Josefin+Slab:wght@300&family=Raleway:wght@400&family=Yellowtail&display=swap" rel="stylesheet">
<style>
  :root {
    --paper: #ffffff;
    --ink: #4a4a4a;
    --accent-red: #d9505e;
    --sun: #f9de8d;
    --petal: #f5c9dd;
    --card: #f2f6f9;
    --hero-yellow: #f6e36a;
    --chalk: #3b3b3b;
    --chalk-light: #4a4a4a;
    --logo-blue: #8fcfd6;
  }
  * { box-sizing: border-box; margin: 0; padding: 0; }
  html, body { width: 731px; height: 1200px; overflow: hidden; background: var(--paper); }
  .page { position: relative; width: 731px; height: 1200px; font-family: "Arvo", serif; color: var(--ink); }

  .site-header { position: absolute; top: 0; left: 0; width: 731px; height: 64px; background: var(--paper); }
  .brand { position: absolute; left: 19px; top: 22px; display: flex; align-items: center; gap: 10px;
    font-family: "Raleway", sans-serif; font-size: 20px; letter-spacing: 7px; color: var(--logo-blue); }
  .brand-dot { width: 12px; height: 12px; border-radius: 50%; background: var(--logo-blue); }
  .main-nav { position: absolute; top: 29px; left: 0; width: 731px; }
  .main-nav a { position: absolute; font-family: "Arvo", serif; font-size: 13.5px; color: var(--ink); text-decoration: none; }
  .nav-active-bar { position: absolute; left: 399px; top: 51px; width: 63px; height: 7px; background: var(--accent-red); }

  .hero { position: absolute; top: 64px; left: 0; width: 731px; height: 345px;
    background:
      radial-gradient(circle at 8% 20%, #c8375a 0 30px, transparent 60px),
      radial-gradient(circle at 92% 85%, #d8425f 0 40px, transparent 80px),
      radial-gradient(circle at 85% 10%, #e0508a 0 25px, transparent 55px),
      radial-gradient(circle at 20% 90%, #c53a4e 0 35px, transparent 70px),
      linear-gradient(160deg, #2f3a2c, #3c4a35 50%, #2c3329);
  }
  .hero-title { position: absolute; top: 118px; left: 0; width: 731px; text-align: center; font-size: 86px; line-height: 1; color: var(--hero-yellow); white-space: nowrap; }
  .hero-title .bold { font-family: "Arvo", serif; font-weight: 700; letter-spacing: 9px; }
  .hero-title .thin { font-family: "Josefin Slab", serif; font-weight: 300; letter-spacing: 16px; }
  .hero-sub { position: absolute; top: 204px; left: 0; width: 731px; text-align: center; font-family: "Yellowtail", cursive; font-size: 38px; line-height: 50px; color: #f4f1e6; }
  .hero-button { position: absolute; left: 309px; top: 272px; width: 133px; height: 32px; background: #f6f3ea;
    font-family: "Raleway", sans-serif; font-size: 12px; letter-spacing: 2px; color: var(--ink); text-align: center; line-height: 32px; }

  .divider { position: absolute; top: 409px; left: 0; width: 731px; height: 28px; }

  .collections { position: absolute; top: 416px; left: 0; width: 731px; height: 568px; background: var(--sun); }
  .collections-panel { position: absolute; left: 59px; top: 0; width: 610px; height: 568px; background: var(--petal); border-left: 1px solid #d4b0a4; border-right: 1px solid #d4b0a4; }
  .section-title { position: absolute; left: 15px; top: 26px; font-family: "Arvo", serif; font-size: 27px; color: #fff;
    text-shadow: 1px 1px 0 #b89aa7, 2px 2px 0 #b89aa7; }
  .collection-card { position: absolute; width: 145px; }
  .collection-photo { width: 145px; height: 142px; }
  .collection-label { width: 145px; height: 52px; background: var(--card); padding: 9px 10px; font-family: "Arvo", serif; font-size: 15px; line-height: 19px; color: #333; }

  .site-footer { position: absolute; top: 984px; left: 0; width: 731px; height: 216px;
    background: radial-gradient(ellipse at 50% 40%, var(--chalk-light), var(--chalk) 70%, #2e2e2e); color: #fff;
    font-family: Arial, Helvetica, sans-serif; font-size: 10.5px; font-weight: 700; line-height: 13px; }
  .footer-col { position: absolute; top: 54px; }
  .footer-col h3 { font-size: 10.5px; font-weight: 700; margin-bottom: 22px; }
  .signup { display: flex; gap: 2px; margin-top: 14px; }
  .signup-field { width: 121px; height: 18px; background: #fff; color: #333; padding-left: 6px; line-height: 18px; }
  .signup-button { width: 52px; height: 18px; background: var(--accent-red); color: #fff; text-align: center; line-height: 18px; }
  .copyright { position: absolute; top: 193px; left: 0; width: 731px; text-align: center; }
</style>
</head>
<body>
<div class="page">
  <header class="site-header">
    <div class="brand"><span class="brand-dot"></span>BRISA PETALS</div>
    <nav class="main-nav">
      <a style="left:413px">HOME</a>
      <a style="left:476px">SHOP</a>
      <a style="left:537px">CURATED</a>
      <a style="left:625px">ABOUT US</a>
    </nav>
    <div class="nav-active-bar"></div>
  </header>

  <section class="hero" role="img" aria-label="Photo of pink and red roses among dark green leaves">
    <h1 class="hero-title"><span class="bold">BAJA</span><span class="thin">FLOR.</span></h1>
    <p class="hero-sub">spring collection</p>
    <div class="hero-button">VIEW NOW.</div>
  </section>

  <section class="collections">
    <div class="collections-panel">
      <h2 class="section-title">Fresh this week</h2>
      <div class="collection-card" style="left:34px;top:80px">
        <div class="collection-photo" role="img" aria-label="Photo of pink and white lilies" style="background:linear-gradient(160deg,#e9dbe2,#7c9a5e 60%,#5f6e48)"></div>
        <div class="collection-label">Any Occasion<br>2 products</div>
      </div>
      <div class="collection-card" style="left:234px;top:80px">
        <div class="collection-photo" role="img" aria-label="Photo of pink gerbera daisies wrapped in kraft paper" style="background:linear-gradient(160deg,#c9a784,#e0578b 50%,#6b8a4d)"></div>
        <div class="collection-label">Birthday<br>1 product</div>
      </div>
      <div class="collection-card" style="left:427px;top:80px">
        <div class="collection-photo" role="img" aria-label="Photo of white calla lilies on dark wood" style="background:linear-gradient(160deg,#3f4347,#d9dccf 45%,#5c6e3c)"></div>
        <div class="collection-label">Dude<br>1 product</div>
      </div>
      <div class="collection-card" style="left:34px;top:325px">
        <div class="collection-photo" role="img" aria-label="Photo of a pile of red roses" style="background:linear-gradient(160deg,#8a1a24,#b3263a 50%,#6d1a1f)"></div>
        <div class="collection-label">Love<br>1 product</div>
      </div>
      <div class="collection-card" style="left:234px;top:325px">
        <div class="collection-photo" role="img" aria-label="Photo of yellow and orange lilies on kraft paper" style="background:linear-gradient(160deg,#7b7a6c,#e9c93f 45%,#e0722f 70%,#c9aa80)"></div>
        <div class="collection-label">Thank you<br>1 product</div>
      </div>
    </div>
  </section>

  <svg class="divider" viewBox="0 0 731 28" width="731" height="28" aria-hidden="true">
    <rect x="0" y="0" width="731" height="7" fill="#d9505e"/>
    <polygon points="356,7 408,7 382,27" fill="#d9505e"/>
  </svg>

  <footer class="site-footer">
    <div class="footer-col" style="left:30px">
      <h3>Meet Brisa &gt;</h3>
      <p>Based in Palmview, San Diego<br>We bring field grown, hand picked,<br>bright, and same day bouquets to your door.<br>ChatterFriendbookSnapgram</p>
    </div>
    <div class="footer-col" style="left:306px">
      <h3>Reach Brisa &gt;</h3>
      <p>2280 Jacaranda Row<br>San Diego, CA 92110<br>Email: info@brisapetals.example<br>Phone: 619-555-0142</p>
    </div>
    <div class="footer-col" style="left:525px">
      <h3>Newsletter &gt;</h3>
      <p>We promise to only send you good<br>things like discounts!</p>
      <div class="signup"><div class="signup-field">Your Email</div><div class="signup-button">Sign up</div></div>
    </div>
    <p class="copyright">Copyright © 2014 brisapetals of San Diego. Website builder by Quillcart.</p>
  </footer>
</div>
</body>
</html>
```